Website Design for Coastal Power Works

We design and install solar power systems for homes and businesses. We also provide engineering services for commercial and utility scale projects

```html
<!DOCTYPE html>
<html lang="en">
<head>
<meta charset="UTF-8">
<title>Coastal Power Works</title>
<link href="https://fonts.googleapis.com/css2?family=Lato:wght@300;400;700;900&family=Oswald:wght@300;400&display=swap" rel="stylesheet">
<style>
  :root {
    --page: #ffffff;
    --green: #8cc63e;
    --orange: #f7931e;
    --orange-text: #f39221;
    --magenta: #ff00ff;
    --footer: #9b9b9b;
    --white: #ffffff;
    --brand-red: #c7362a;
    --ink: #333333;
    --field-border: #cccccc;
  }
  * { margin: 0; padding: 0; box-sizing: border-box; }
  html, body { width: 1200px; height: 863px; overflow: hidden; background: var(--page); }
  body { position: relative; font-family: "Lato", sans-serif; }

  .brand { position: absolute; left: 183px; top: 64px; display: flex; align-items: center; gap: 8px; }
  .brand-dot { width: 14px; height: 14px; border-radius: 50%; background: var(--brand-red); }
  .brand-name { font-family: "Lato", sans-serif; font-weight: 700; font-size: 15px; color: var(--ink); letter-spacing: 0.5px; text-transform: uppercase; }

  .search { position: absolute; left: 783px; top: 25px; width: 248px; height: 26px; border: 1px solid #cfcfcf; border-radius: 3px; background: #fff; }
  .search svg { position: absolute; right: 4px; top: 2px; }

  .tagline { position: absolute; right: 175px; top: 100px; font-family: "Lato", sans-serif; font-weight: 300; font-size: 17px; color: var(--orange-text); }
  .callout { position: absolute; right: 175px; top: 124px; font-family: "Lato", sans-serif; font-weight: 700; font-size: 17px; color: var(--orange-text); }

  .tile { position: absolute; overflow: hidden; }
  .tile-residential { left: 183px; top: 147px; width: 273px; height: 273px; background: var(--green); }
  .tile-commercial { left: 752px; top: 147px; width: 273px; height: 273px; background: var(--orange); }
  .tile-hills { left: 472px; top: 147px; width: 264px; height: 273px; background: linear-gradient(180deg, #1f6fd6 0%, #5fa7ee 45%, #9fd0f5 58%, #6fb52e 66%, #3f8d1c 100%); }
  .tile-family { left: 183px; top: 437px; width: 273px; height: 266px; background: linear-gradient(180deg, #e9c08a 0%, #f3d6a8 40%, #d9953f 70%, #5a3a1c 100%); }
  .tile-array { left: 752px; top: 437px; width: 273px; height: 266px; background: linear-gradient(180deg, #3e7fd0 0%, #86b6e6 55%, #c7d8e4 72%, #39424e 80%, #8a7a4e 100%); }
  .tile-quote { left: 472px; top: 437px; width: 264px; height: 266px; background: var(--magenta); }

  .tile-icon { position: absolute; left: 50%; transform: translateX(-50%); }
  .tile-residential .tile-icon { top: 89px; }
  .tile-commercial .tile-icon { top: 82px; }
  .tile-label { position: absolute; left: 0; right: 0; top: 218px; text-align: center; color: var(--white); font-weight: 700; font-size: 26px; }

  .quote-title { position: absolute; left: 0; right: 0; top: 18px; text-align: center; color: var(--white); font-weight: 900; font-size: 26px; }
  .quote-field { position: absolute; left: 23px; width: 222px; height: 25px; background: #fff; border: 1px solid var(--field-border); font-family: "Lato", sans-serif; font-size: 12px; color: #999; padding: 0 8px; line-height: 23px; }
  .field-name { top: 83px; }
  .field-email { top: 123px; }
  .field-phone { top: 163px; }
  .quote-submit { position: absolute; left: 203px; top: 218px; }

  .site-footer { position: absolute; left: 183px; top: 720px; width: 842px; height: 143px; background: var(--footer); color: var(--white); font-family: "Oswald", sans-serif; font-weight: 300; }
  .footer-col { position: absolute; top: 4px; }
  .footer-col h3 { font-weight: 300; font-size: 16px; line-height: 22px; }
  .footer-col ul { list-style: none; margin-top: 8px; font-size: 13px; line-height: 17px; }
  .col-about { left: 5px; }
  .col-solar { left: 185px; }
  .col-residential { left: 397px; }
  .col-business { left: 596px; }
  .col-contact { right: 10px; text-align: right; }
  .col-contact ul { font-size: 12px; }
  .follow { position: absolute; left: 5px; top: 112px; display: flex; align-items: center; gap: 5px; font-size: 16px; }
  .social { width: 24px; height: 24px; border-radius: 2px; }
  .social-a { background: #3b5a9a; margin-left: 2px; }
  .social-b { background: #2aa3d9; }
  .social-c { background: #5b8f3a; }
  .copyright { position: absolute; left: 328px; top: 121px; font-size: 11px; }
  .legal { position: absolute; right: 10px; top: 118px; font-size: 13px; }
</style>
</head>
<body>
  <header>
    <div class="brand"><span class="brand-dot"></span><span class="brand-name">Coastal Power Works</span></div>
    <div class="search">
      <svg width="22" height="22" viewBox="0 0 22 22"><circle cx="8" cy="8" r="5" fill="none" stroke="#888" stroke-width="1.5"/><line x1="12" y1="12" x2="19" y2="18" stroke="#666" stroke-width="2.5" stroke-linecap="round"/></svg>
    </div>
    <p class="tagline">Reduce electricity cost</p>
    <p class="callout">Call us: 02 5550 1927 or Email: info@coastalpowerworks.com</p>
  </header>

  <main>
    <a class="tile tile-residential">
      <svg class="tile-icon" width="94" height="94" viewBox="0 0 94 94">
        <circle cx="47" cy="47" r="44" fill="none" stroke="#fff" stroke-width="4"/>
        <path d="M25 48 L47 28 L69 48 L63 48 L63 64 L52 64 L52 54 L42 54 L42 64 L31 64 L31 48 Z" fill="#fff"/>
      </svg>
      <span class="tile-label">Residential</span>
    </a>
    <div class="tile tile-hills" role="img" aria-label="Solar panels standing on rolling green hills under a blue sky"></div>
    <a class="tile tile-commercial">
      <svg class="tile-icon" width="94" height="94" viewBox="0 0 94 94">
        <circle cx="47" cy="47" r="44" fill="none" stroke="#fff" stroke-width="4"/>
        <circle cx="47" cy="38" r="11" fill="none" stroke="#fff" stroke-width="3.5"/>
        <path d="M28 66 Q28 52 47 52 Q66 52 66 66 Z" fill="none" stroke="#fff" stroke-width="3.5" stroke-linejoin="round"/>
      </svg>
      <span class="tile-label">Commercial</span>
    </a>

    <div class="tile tile-family" role="img" aria-label="Silhouette of a parent and child walking through a field at sunset"></div>
    <form class="tile tile-quote">
      <h2 class="quote-title">Free Online Quote</h2>
      <div class="quote-field field-name">Full name</div>
      <div class="quote-field field-email">Email</div>
      <div class="quote-field field-phone">Phone</div>
      <svg class="quote-submit" width="44" height="44" viewBox="0 0 44 44">
        <circle cx="22" cy="22" r="19" fill="none" stroke="#fff" stroke-width="3"/>
        <path d="M12 22 H30 M23 14 L31 22 L23 30" fill="none" stroke="#fff" stroke-width="3.5" stroke-linecap="round" stroke-linejoin="round"/>
      </svg>
    </form>
    <div class="tile tile-array" role="img" aria-label="Ground-mounted solar panel array in an open field under a clear sky"></div>
  </main>

  <footer class="site-footer">
    <div class="footer-col col-about"><h3>About us</h3></div>
    <div class="footer-col col-solar"><h3>It's all about solar</h3><ul><li>Sunny Notes</li><li>The Sun</li></ul></div>
    <div class="footer-col col-residential"><h3>Residential</h3></div>
    <div class="footer-col col-business"><h3>Business</h3><ul><li>Applications</li><li>Benefits</li><li>Success Stories</li></ul></div>
    <div class="footer-col col-contact"><h3>Contact</h3><ul><li>02 5550 1927</li><li>info@coastalpowerworks.com.au</li></ul></div>
    <div class="follow">Follow us on......
      <span class="social social-a"></span><span class="social social-b"></span><span class="social social-c"></span>
    </div>
    <p class="copyright">Coastal Power Works 2013 © - All rights reserved</p>
    <p class="legal">Sitemap | Privacy Policy | Terms of use</p>
  </footer>
</body>
</html>
```